Marwick Law Letterhead

We need a new letterhead design for a Law Firm. The address for the law firm is 4175 Calloway Avenue, Suite 200, Houston, Texas 77046. Phone Number: 832-614-2093; Fax Number: 832-307-1546. The logo is uploaded to the project.

```html
<!DOCTYPE html>
<html lang="en">
<head>
<meta charset="utf-8">
<title>Marwick Law Letterhead</title>
<link href="https://fonts.googleapis.com/css2?family=Open+Sans:wght@400;600&family=Lato:wght@400&display=swap" rel="stylesheet">
<style>
  :root {
    --navy: #142c57;
    --red: #e01f26;
    --ink: #3f3f3f;
    --paper: #ffffff;
    --sig: #e6e8ee;
  }
  * { margin: 0; padding: 0; box-sizing: border-box; }
  html, body { width: 1040px; height: 1200px; overflow: hidden; background: var(--paper); }
  .letterhead {
    position: relative;
    width: 1040px;
    height: 1200px;
    background: var(--paper);
    font-family: "Open Sans", sans-serif;
    color: var(--ink);
  }
  .top-bar { position: absolute; top: 0; left: 0; width: 100%; height: 14px; display: flex; gap: 6px; }
  .top-bar .navy { flex: 0 0 692px; background: var(--navy); }
  .top-bar .red { flex: 1; background: var(--red); }

  .brand { position: absolute; top: 36px; left: 100px; display: flex; align-items: center; gap: 14px; }
  .brand-square { width: 42px; height: 42px; background: var(--navy); }
  .brand-name { font-family: "Open Sans", sans-serif; font-weight: 600; font-size: 38px; color: var(--navy); letter-spacing: 0.5px; }

  .contact { position: absolute; top: 38px; left: 700px; padding-left: 14px; border-left: 2px solid var(--navy); height: 66px; display: flex; flex-direction: column; justify-content: center; gap: 2px; }
  .contact-line { display: flex; align-items: center; gap: 10px; font-family: "Lato", sans-serif; font-size: 19px; color: #111; }
  .contact-line svg { width: 18px; height: 18px; fill: var(--navy); }

  .letter { position: absolute; top: 238px; left: 98px; width: 842px; font-size: 15.5px; }
  .issue-date { margin-bottom: 18px; }
  .recipient { line-height: 19px; margin-bottom: 48px; }
  .salutation { margin-bottom: 26px; }
  .letter p.body { line-height: 30px; text-align: justify; hyphens: auto; margin-bottom: 24px; }
  .closing { margin-top: 46px; }
  .signature { width: 230px; height: 34px; margin: 14px 0 10px; background: var(--sig); border-radius: 3px; }
  .signer-name { font-size: 19px; color: #2a2a2a; }
  .signer-role { margin-top: 6px; }

  .footer-wave { position: absolute; left: 0; bottom: 0; width: 1040px; height: 200px; }
  .address { position: absolute; left: 103px; top: 1109px; font-family: "Lato", sans-serif; font-size: 19px; color: #111; }
</style>
</head>
<body>
<div class="letterhead">
  <div class="top-bar"><div class="navy"></div><div class="red"></div></div>

  <div class="brand">
    <div class="brand-square"></div>
    <div class="brand-name">Marwick Law</div>
  </div>

  <div class="contact">
    <div class="contact-line">
      <svg viewBox="0 0 24 24" aria-hidden="true"><path d="M6.6 10.8a15.1 15.1 0 0 0 6.6 6.6l2.2-2.2a1 1 0 0 1 1-.25 11.4 11.4 0 0 0 3.6.57 1 1 0 0 1 1 1V20a1 1 0 0 1-1 1A17 17 0 0 1 3 4a1 1 0 0 1 1-1h3.5a1 1 0 0 1 1 1c0 1.25.2 2.45.57 3.6a1 1 0 0 1-.25 1z"/></svg>
      <span>832-614-2093</span>
    </div>
    <div class="contact-line">
      <svg viewBox="0 0 24 24" aria-hidden="true"><path d="M6 2h12v6H6zM4 9h16a2 2 0 0 1 2 2v6h-4v5H6v-5H2v-6a2 2 0 0 1 2-2zm4 8v3h8v-3z"/></svg>
      <span>832-307-1546</span>
    </div>
  </div>

  <main class="letter">
    <div class="issue-date">Issuing Date: May 5, 2018</div>
    <div class="recipient">Name Of Employee Mr. XYZABC<br>Address of Employee<br>Address Line 2 etc..</div>
    <div class="salutation">Dear Mr.XYZABC</div>
    <p class="body">Lorem Ipsum has been the industry's standard dummy text ever since the 1500s, when an unknown printer took a galley of type and scrambled it to make a type specimen book. It has survived not only five centuries, but also the leap into electronic typesetting, remaining essentially unchanged. It was popularised in the 1960s with the release of Linotext sheets containing Lorem Ipsum passages, and more recently with desktop publishing software like Ardent PageSetter including versions of Lorem Ipsum.</p>
    <p class="body">Lorem Ipsum is simply dummy text of the printing and typesetting industry. Lorem Ipsum has been the industry's standard dummy text ever since the 1500s, when an unknown printer took a galley of type and scrambled it to make a type specimen book.</p>
    <p class="body">It has survived not only five centuries, but also the leap into electronic typesetting, remaining essentially unchanged. It was popularised in the 1960s with the release of Linotext sheets containing Lorem Ipsum passages.</p>
    <div class="closing">Yours Sincerely</div>
    <div class="signature" role="img" aria-label="Handwritten signature of Daniel Whitford"></div>
    <div class="signer-name">Daniel Whitford</div>
    <div class="signer-role">Managing Director</div>
  </main>

  <svg class="footer-wave" viewBox="0 0 1040 200" preserveAspectRatio="none" aria-hidden="true">
    <path fill="var(--navy)" d="M1040,13 C900,128 620,172 0,172 L0,200 L1040,200 Z"/>
    <path fill="var(--red)" d="M0,148 C420,168 800,138 965,60 C810,148 430,178 0,168 Z"/>
  </svg>
  <div class="address">4175 Calloway Avenue, Suite 200, Houston, Texas 77046</div>
</div>
</body>
</html>
```